Top Real Estate teams new cards UPDATED

New Cards with MY (Im the tall guy in the middle) new pic on the front of card and my team pic on the back of card. Also my team name on the front of the card (marlow and partners) and brokerage name on the back (harborline real estate group) . Also the tag line "Ask about our 20 step plan" on the back of the card and "Welcome to the new way of Real Estate Sales" on the front of the card along with my phone number (951-284-7310) and email address (devon.marlow47@quillmail.net) my website (www.DevonMarlow.org) and my License number (BRE:07315942). I do like my team name colors of black and gold
Logo links are attached:
1. https://www.filecrate.net/sh/918kqwz72pavdle/AAF7QmR2HtK4BnYwPzLxUe_KGb?dl=0
2. https://www.filecrate.net/sh/27w5xvn81rbt094/AACKTJMR46DnQ2Wf7RyGs8Vh3b?dl=0
Updates

Target Market(s)

Real Estate Customers

Industry/Entity Type

Real Estate

Contact Information for Business Card

Classy, yet east ro read and understand

Font styles to use
Sans Serif

Requirements
Must have
• Team and brokerage name, and both slogans.
• Black and gold color scheme.
Nice to have
• Bold writing
Should not have
• cluttered feeling

```html
<!DOCTYPE html>
<html lang="en">
<head>
<meta charset="utf-8">
<title>Marlow and Partners – Business Cards</title>
<link rel="stylesheet" href="https://fonts.googleapis.com/css2?family=Lato:ital,wght@0,400;0,700;0,900;1,900&display=swap">
<style>
  :root {
    --gold: #c49a22;
    --black: #070707;
    --ink: #1e1b1b;
    --icon-green: #1f9d55;
    --white: #ffffff;
    --backdrop: #d9d9d9;
  }
  * { margin: 0; padding: 0; box-sizing: border-box; }
  html, body { width: 1200px; height: 1000px; overflow: hidden; }
  body {
    background: var(--backdrop);
    font-family: "Lato", Arial, sans-serif;
    position: relative;
  }
  .card {
    position: absolute;
    width: 725px;
    height: 425px;
    overflow: hidden;
    background: var(--black);
  }
  .card--front { left: 118px; top: 80px; }
  .card--back { left: 340px; top: 520px; }
  .card__bands { position: absolute; inset: 0; }

  /* Front */
  .team-mark {
    position: absolute;
    left: 22px; top: 22px;
    width: 190px;
    text-align: center;
    color: var(--ink);
  }
  .team-mark__dot {
    width: 50px; height: 50px; border-radius: 50%;
    background: var(--ink);
    margin: 0 auto 6px;
  }
  .team-mark__name {
    font-size: 22px; line-height: 1.05; font-weight: 400;
    text-transform: uppercase; letter-spacing: 0.5px;
  }
  .agent-name {
    position: absolute;
    left: 365px; top: 46px;
    font-size: 30px; font-weight: 900; font-style: italic;
    color: var(--ink);
    letter-spacing: -0.5px;
    white-space: nowrap;
  }
  .contact {
    position: absolute;
    display: flex; align-items: center; gap: 14px;
    font-size: 17px; color: var(--gold);
    white-space: nowrap;
  }
  .contact__icon { width: 20px; display: flex; justify-content: center; color: var(--icon-green); }
  .contact__label { color: var(--icon-green); font-size: 16px; }
  .contact--phone { left: 98px; top: 164px; }
  .contact--license { left: 98px; top: 200px; gap: 12px; }
  .contact--email { left: 98px; top: 234px; }
  .contact--web { left: 424px; top: 234px; }
  .tagline {
    position: absolute;
    left: 234px; top: 340px;
    font-size: 18px; font-weight: 400;
    letter-spacing: -0.2px;
    color: var(--black);
    text-transform: uppercase;
    transform: rotate(-5.6deg);
    transform-origin: left center;
    white-space: nowrap;
  }
  .brokerage-badge {
    position: absolute;
    background: #000;
    color: var(--white);
    display: flex; align-items: center; justify-content: center;
    text-align: center;
    text-transform: uppercase;
    font-size: 8px; line-height: 1.2; letter-spacing: 0.3px;
    padding: 4px;
  }
  .card--front .brokerage-badge { left: 15px; top: 365px; width: 88px; height: 57px; }

  /* Back */
  .offer {
    position: absolute;
    left: 48px; top: 64px;
    color: var(--gold);
    font-weight: 900;
    font-size: 28px;
    font-variant: small-caps;
    letter-spacing: 0.3px;
    transform: rotate(-4deg);
    transform-origin: left center;
    white-space: nowrap;
  }
  .offer__number { font-size: 30px; }
  .team-photo {
    position: absolute;
    left: 482px; top: 68px;
    width: 190px; height: 205px;
    background: linear-gradient(180deg, #2a2420 0%, #111 70%, #0a0a0a 100%);
  }
  .team-seal {
    position: absolute;
    left: 40px; top: 278px;
    width: 150px; height: 150px;
    border-radius: 50%;
    background: var(--ink);
    color: var(--gold);
    display: flex; align-items: center; justify-content: center;
    text-align: center;
    text-transform: uppercase;
    font-size: 17px; line-height: 1.15;
  }
  .card--back .brokerage-badge { left: 612px; top: 330px; width: 96px; height: 66px; }
</style>
</head>
<body>

<section class="card card--front" aria-label="Business card front">
  <svg class="card__bands" width="725" height="425" viewBox="0 0 725 425" aria-hidden="true">
    <rect width="725" height="425" fill="var(--black)"/>
    <polygon points="0,0 725,0 725,78 0,162" fill="var(--gold)"/>
    <polygon points="0,335 725,262 725,380 262,425" fill="var(--gold)"/>
  </svg>

  <div class="team-mark">
    <div class="team-mark__dot"></div>
    <div class="team-mark__name">Marlow and<br>Partners</div>
  </div>

  <div class="agent-name">Devon Marlow</div>

  <div class="contact contact--phone">
    <span class="contact__icon">
      <svg width="18" height="10" viewBox="0 0 18 10"><path d="M1 6 C3 1 15 1 17 6 L17 9 L13 9 L13 6 C11 5 7 5 5 6 L5 9 L1 9 Z" fill="currentColor"/></svg>
    </span>
    <span>951-284-7310</span>
  </div>
  <div class="contact contact--license">
    <span class="contact__label">Lic:</span>
    <span>BRE:07315942</span>
  </div>
  <div class="contact contact--email">
    <span class="contact__icon">
      <svg width="18" height="13" viewBox="0 0 18 13"><rect x="0" y="0" width="18" height="13" fill="currentColor"/><path d="M1 1 L9 7 L17 1" stroke="var(--black)" stroke-width="1.2" fill="none"/></svg>
    </span>
    <span>devon.marlow47@quillmail.net</span>
  </div>
  <div class="contact contact--web">
    <span class="contact__icon">
      <svg width="15" height="15" viewBox="0 0 16 16"><circle cx="8" cy="8" r="7" fill="none" stroke="currentColor" stroke-width="1.6"/><ellipse cx="8" cy="8" rx="3" ry="7" fill="none" stroke="currentColor" stroke-width="1.2"/><line x1="1" y1="8" x2="15" y2="8" stroke="currentColor" stroke-width="1.2"/></svg>
    </span>
    <span>www.DevonMarlow.org</span>
  </div>

  <div class="tagline">Welcome to the new way of real estate sales</div>

  <div class="brokerage-badge">Harborline Real Estate Group</div>
</section>

<section class="card card--back" aria-label="Business card back">
  <svg class="card__bands" width="725" height="425" viewBox="0 0 725 425" aria-hidden="true">
    <rect width="725" height="425" fill="var(--black)"/>
    <polygon points="0,350 725,228 725,425 0,425" fill="var(--gold)"/>
  </svg>

  <div class="offer">Ask about our <span class="offer__number">20</span> step plan</div>

  <div class="team-photo" role="img" aria-label="Photo of the three team members standing in black formal wear"></div>

  <div class="team-seal">Marlow and<br>Partners</div>

  <div class="brokerage-badge">Harborline Real Estate Group</div>
</section>

</body>
</html>
```